依頼詳細
グローバルナビ
左サイドメニュー
横幅:960px

今回は、コンペ用のデザイン作成依頼となります。ロゴや電話番号・その他画像データ等サンプルで作成頂ければ幸いです。

《クライアント様からの要望》
すっきりとした見やすいホームページで、患者様やご家族の方に優しい・温かいイメージをもって欲しい。
ロゴに使用されているカラーコードは、「24569d」となります。基調色として取り入れてください。

総合病院で診療科目が多い為、利用者が情報を探しやすいように工夫してください。
病院のPRポイントとしては、「救急患者の受入れを断らない」地域に最先端医療で貢献する。等

(topページに必要なコンテンツ)
・病院からのお知らせ
・はじめてご来院の方へ
-外来受診のご案内
-診療担当・日時
-休診・代診のお知らせ
-入院のご案内
-セカンドオピニオンについて
・お見舞いの皆様へ
・診療科・施設のご案内
-※別途、診療科・施設については添付ファイルを参照ください。
・当院の紹介
・採用情報
・先進医療センター
・周産期医療センター
・消化器病センター
・乳腺診療センター
・地域医療連携への取り組み
サイトURL
ページ数
1ページ
希望イメージ
シンプル 複雑
単色 カラフル
暗い 明るい
日常 高級
遊び心 厳粛
未来的 伝統的
女性的 男性的
希望する色
ブルーを基調(ロゴカラーコード:24569d)差し色はお任せ
納品ファイル
• フォトショップ形式 (.psd)
• PNG形式 (.png)
補足説明
デザインの作成は、Photoshop・Fireworksのみとなります。Illustratorでの作成は不可とします。
(デザイン参考URL)
http://www.tomebara-kouaikai.gr.jp/
http://www.hinokidai.or.jp/
http://kobu.ntmsu.ac.jp/

現サイトのURLにつきましては、個別にメッセージにてお送りさせて頂きますので、希望される方はメッセージをお送りください。
診療科・その他施設一覧ファイルを追加しました。
既存サイトのURLをお伝えした場合、既存サイトのデザインと同じようなご提案が多いため、期間を延長させて頂きます。
既存サイトのURLはお伝えしませんので、斬新なデザインのご提案をお待ちしております。

全体的にスッキリとしている。病院側の伝えたいポイントをしっかりと捉えている。見やすい等、選定理由となりました。

今回、デザイン作成に応募いただきましてありがとうございます。ご提案いただきました全てのデザインをクライアント様に確認いただき、選定させていただきました。
今後とも、機会がありましたら宜しくお願いいたします。

```html
<!DOCTYPE html>
<html lang="ja">
<head>
<meta charset="utf-8">
<title>病院トップページ</title>
<link rel="stylesheet" href="https://fonts.googleapis.com/css2?family=Noto+Sans+JP:wght@400;700&family=Noto+Serif+JP:wght@700&display=swap">
<style>
:root{
  --brand:#24569d;
  --brand-dark:#173d73;
  --sky:#e6eff9;
  --sky-2:#cfdff1;
  --line:#b9cde6;
  --text:#333;
  --muted:#666;
  --accent:#f0a24a;
  --accent-soft:#fbe3c2;
  --white:#fff;
}
*{margin:0;padding:0;box-sizing:border-box}
html,body{width:824px;height:1200px;overflow:hidden}
body{font-family:"Noto Sans JP",sans-serif;color:var(--text);background:linear-gradient(90deg,var(--sky) 0,var(--white) 14px,var(--white) 810px,var(--sky) 824px);font-size:13px}
.page{position:relative;width:824px;height:1200px}

.site-header{height:92px;background:linear-gradient(#fff,#f3f7fc);position:relative}
.logo{position:absolute;left:24px;top:12px;font-size:30px;font-weight:700;color:var(--brand);letter-spacing:2px}
.util-links{position:absolute;right:40px;top:14px;display:flex;gap:28px;font-size:14px;color:var(--brand)}
.util-links span{display:flex;align-items:center;gap:6px}
.util-links i{width:20px;height:14px;background:var(--brand);border-radius:3px;display:inline-block}
.tagline{position:absolute;left:190px;top:56px;width:620px;height:26px;background:var(--sky);border:1px solid var(--line);font-size:14px;color:var(--brand);display:flex;align-items:center;padding-left:12px}

.global-nav{display:flex;height:52px;margin:6px 14px 0;border-bottom:3px solid var(--accent)}
.global-nav a{flex:1;text-decoration:none;color:var(--brand);font-size:13px;line-height:1.3;background:linear-gradient(#f7fafd,#e3ecf7);border:1px solid var(--line);border-bottom:none;margin-right:3px;display:flex;align-items:center;padding-left:10px}
.global-nav a.current{background:linear-gradient(#fde9cf,var(--accent-soft));color:var(--text);justify-content:center;font-weight:700}
.global-nav a:last-child{margin-right:0}

.breadcrumb{margin:6px 14px 0;background:var(--sky);height:22px;font-size:12px;color:var(--brand);padding:3px 10px}

.hero{margin:12px 14px 0;height:150px;display:flex;background:linear-gradient(#fff,#f3f7fc)}
.hero-copy{flex:1;padding:38px 0 0 34px;font-family:"Noto Serif JP",serif;color:var(--brand)}
.hero-copy .lead{font-size:27px}
.hero-copy .sub{font-size:20px;margin:18px 0 0 170px}
.hero-photo{width:300px;height:150px;background:linear-gradient(160deg,#dbe8f5,#9fb8d4 60%,#7d98b8)}

.body{display:flex;margin:16px 14px 0;gap:16px}
.side-menu{width:190px;display:flex;flex-direction:column;gap:11px}
.side-menu a{height:46px;text-decoration:none;color:var(--brand);font-size:14px;background:linear-gradient(#fff,#eef3f9);border:1px solid var(--line);display:flex;align-items:center;gap:8px;padding-left:8px}
.side-menu a b{width:30px;height:30px;background:var(--sky-2);flex:none}
.side-menu a.first{background:linear-gradient(#fff,#fdf1e0);border-color:#e8c9a0}
.side-menu a.first b{background:var(--accent-soft)}

.main{flex:1}
.panel-title{height:30px;border:1px solid var(--line);background:linear-gradient(#fff,#eef3f9);font-size:13px;color:var(--text);display:flex;align-items:center;padding-left:10px;gap:6px}
.panel-title::before{content:"";border-left:6px solid var(--accent);border-top:4px solid transparent;border-bottom:4px solid transparent}
.news{list-style:none;padding:10px 0 18px 80px}
.news li{display:flex;gap:56px;font-size:13px;line-height:26px}
.recruit{margin:18px 0 0 250px;width:156px;height:28px;border:1px solid var(--line);background:linear-gradient(#fff,#eef3f9);font-size:12px;color:var(--muted);display:flex;align-items:center;justify-content:center}

.site-footer{position:absolute;left:14px;right:14px;top:790px;height:354px;background:var(--sky);display:flex;padding:26px 0 0 44px;gap:0}
.dept-col{width:230px;font-size:12px;line-height:17px;color:var(--brand)}
.dept-col .group{margin-bottom:18px}
.dept-col .head{font-weight:700}
.copyright{position:absolute;left:0;right:0;bottom:0;height:56px;background:var(--brand-dark);color:var(--white);font-size:13px;display:flex;align-items:center;justify-content:center}
</style>
</head>
<body>
<div class="page">
  <header class="site-header">
    <div class="logo">ロゴマーク</div>
    <div class="util-links"><span><i></i>当院の紹介</span><span><i></i>お問い合わせ</span></div>
    <div class="tagline">「救急患者の受入れを断らない」地域に最先端医療で貢献</div>
  </header>

  <nav class="global-nav">
    <a class="current" href="#">ホーム</a>
    <a href="#">診療担当・<br>日時</a>
    <a href="#">診療科・<br>施設のご案内</a>
    <a href="#">セカンドオピニオン<br>について</a>
    <a href="#">お見舞いの<br>皆様へ</a>
    <a href="#">地域医療連携<br>への取り組み</a>
  </nav>

  <div class="breadcrumb">現在のページ：ホーム</div>

  <section class="hero">
    <div class="hero-copy">
      <p class="lead">「救急患者の受入れを断らない」</p>
      <p class="sub">地域に最先端医療で貢献。</p>
    </div>
    <div class="hero-photo" role="img" aria-label="病院の建物外観の写真"></div>
  </section>

  <div class="body">
    <aside class="side-menu">
      <a class="first" href="#"><b></b>はじめてご来院の方へ</a>
      <a href="#"><b></b>外来受診のご案内</a>
      <a href="#"><b></b>入院のご案内</a>
      <a href="#"><b></b>先進医療センター</a>
      <a href="#"><b></b>周産期医療センター</a>
      <a href="#"><b></b>消化器病センター</a>
      <a href="#"><b></b>乳腺診療センター</a>
    </aside>
    <main class="main">
      <div class="panel-title">病院からのお知らせ</div>
      <ul class="news">
        <li><span>2013-3-18</span><span>サンプルテキスト</span></li>
        <li><span>2013-3-18</span><span>サンプルテキスト</span></li>
        <li><span>2013-3-18</span><span>サンプルテキスト</span></li>
      </ul>
      <div class="panel-title">休診・代診のお知らせ</div>
      <ul class="news">
        <li><span>2012-3-18</span><span>サンプルテキスト</span></li>
        <li><span>2012-3-18</span><span>サンプルテキスト</span></li>
        <li><span>2012-3-18</span><span>サンプルテキスト</span></li>
      </ul>
      <div class="panel-title">採用情報</div>
      <div class="recruit">看護師の募集について</div>
    </main>
  </div>

  <footer class="site-footer">
    <div class="dept-col">
      <div class="group"><p class="head">■放射線科</p><p>-放射線診断科</p><p>-リハビリテーション科</p><p>-麻酔科</p><p>-病理科</p></div>
      <div class="group"><p class="head">■内科</p><p>-総合内科・漢方内科</p><p>-神経内科</p><p>-消化器内科</p><p>-循環器内科</p><p>-呼吸器科</p><p>-腎臓内科</p><p>-糖尿病内科</p></div>
    </div>
    <div class="dept-col">
      <div class="group"><p class="head">■外科</p><p>-内視鏡外科</p><p>-乳腺科</p><p>-脳神経外科</p><p>-心臓血管外科</p><p>-整形外科</p><p>-皮膚科</p><p>-泌尿器科</p><p>-耳鼻咽喉科</p><p>-歯科口腔外科</p><p>-眼科</p><p>-産科</p><p>-婦人科</p></div>
    </div>
    <div class="dept-col">
      <p class="head">(その他、治療・検査施設)</p>
      <p>総合リハビリテーションセンター</p><p>通所リハビリテーションセンター</p><p>在宅医療センター</p><p>検診センター</p><p>手術室</p><p>栄養管理室</p><p>地域リハビリテーション広域支援センター</p><p>消化器病センター</p><p>乳腺診療センター</p><p>先進医療センター</p><p>透析室</p><p>薬局</p><p>臨床検査センター</p><p>ＭＥ室（臨床工学部）</p>
    </div>
    <div class="copyright">Copyright</div>
  </footer>
</div>
</body>
</html>
```